Interior designer needs a gorgeous, chic business card design.

A new, small Interior Design firm needs a business card that is chic, contemporary and elegant. Nothing over the top. My interiors are contemporary classic with an elegant feel to them. I like to use quality finishes and products rather than follow the latest fads. Projects can be anything from Pre start selections, bathrooms, kitchens, bedrooms, custom upholstery, furniture, rugs and art etc. The final design should display quality and an achievable sense of chic. I am open to all colours including black but not limited to this.

```html
<!DOCTYPE html>
<html lang="en">
<head>
<meta charset="utf-8">
<title>Vela Interiors – Business Card</title>
<link rel="stylesheet" href="https://fonts.googleapis.com/css2?family=Cormorant+Garamond:wght@500;600;700&display=swap">
<style>
  :root {
    --page: #e6e6e6;
    --charcoal: #474747;
    --charcoal-deep: #3d3d3d;
    --silver: #f4f4f4;
    --ink: #1f1f1f;
    --white: #ffffff;
  }
  * { margin: 0; padding: 0; box-sizing: border-box; }
  html, body {
    width: 1200px;
    height: 1035px;
    overflow: hidden;
    background: var(--page);
  }
  .sheet {
    position: relative;
    width: 1200px;
    height: 1035px;
  }
  .card {
    position: absolute;
    left: 190px;
    width: 820px;
    height: 468px;
    overflow: hidden;
    box-shadow: 0 6px 18px rgba(0,0,0,0.18);
  }
  .card--back { top: 29px; }
  .card--front { top: 537px; }
  .card__surface {
    position: absolute;
    inset: 0;
    width: 100%;
    height: 100%;
  }
  .wordmark {
    position: absolute;
    white-space: nowrap;
    font-family: "Cormorant Garamond", serif;
    font-weight: 600;
    color: var(--white);
    letter-spacing: 2px;
    line-height: 1;
  }
  .card--back .wordmark {
    left: 0;
    right: 0;
    top: 200px;
    text-align: center;
    font-size: 68px;
  }
  .card--front .wordmark {
    left: 28px;
    top: 44px;
    font-size: 54px;
  }
  .holder {
    position: absolute;
    right: 20px;
    top: 222px;
    text-align: right;
    font-family: "Cormorant Garamond", serif;
    color: var(--ink);
  }
  .holder__name {
    font-size: 40px;
    font-weight: 600;
    line-height: 1;
  }
  .holder__title {
    font-size: 24px;
    font-weight: 700;
    line-height: 1.3;
  }
  .contact {
    position: absolute;
    top: 378px;
    font-family: "Cormorant Garamond", serif;
    font-weight: 700;
    font-size: 25px;
    line-height: 37px;
    color: var(--ink);
    list-style: none;
  }
  .contact--left { left: 28px; }
  .contact--right { left: 470px; }
</style>
</head>
<body>
<main class="sheet">

  <section class="card card--back" aria-label="Card back">
    <svg class="card__surface" viewBox="0 0 820 468" preserveAspectRatio="none" aria-hidden="true">
      <defs>
        <linearGradient id="back-sheen" x1="0" y1="0" x2="1" y2="1">
          <stop offset="0" stop-color="#4d4d4d"/>
          <stop offset="0.35" stop-color="#444444"/>
          <stop offset="0.6" stop-color="#4f4f4f"/>
          <stop offset="1" stop-color="#3f3f3f"/>
        </linearGradient>
      </defs>
      <rect width="820" height="468" fill="url(#back-sheen)"/>
      <path d="M0 60 C250 20 520 120 820 40 V110 C540 190 260 90 0 140 Z" fill="#ffffff" opacity="0.04"/>
      <path d="M0 330 C260 270 540 380 820 300 V360 C540 440 260 330 0 400 Z" fill="#ffffff" opacity="0.035"/>
    </svg>
    <h2 class="wordmark">Vela Interiors</h2>
  </section>

  <section class="card card--front" aria-label="Card front">
    <svg class="card__surface" viewBox="0 0 820 468" preserveAspectRatio="none" aria-hidden="true">
      <defs>
        <linearGradient id="front-silver" x1="0" y1="0" x2="1" y2="1">
          <stop offset="0" stop-color="#fafafa"/>
          <stop offset="0.45" stop-color="#e2e2e2"/>
          <stop offset="0.7" stop-color="#f3f3f3"/>
          <stop offset="1" stop-color="#d9d9d9"/>
        </linearGradient>
        <linearGradient id="front-band" x1="0" y1="0" x2="1" y2="0">
          <stop offset="0" stop-color="#474747"/>
          <stop offset="1" stop-color="#3d3d3d"/>
        </linearGradient>
      </defs>
      <rect width="820" height="468" fill="url(#front-silver)"/>
      <path d="M0 300 C260 240 520 360 820 280 V330 C520 410 260 300 0 360 Z" fill="#ffffff" opacity="0.5"/>
      <path d="M0 0 H640 C710 0 780 30 820 80 V175 C720 120 600 150 480 175 C330 206 160 196 0 192 Z" fill="url(#front-band)"/>
    </svg>
    <h1 class="wordmark">Vela Interiors</h1>
    <div class="holder">
      <p class="holder__name">Your name here</p>
      <p class="holder__title">President</p>
    </div>
    <ul class="contact contact--left">
      <li>Phone : Your phone number</li>
      <li>Facebook : facebookURL</li>
    </ul>
    <ul class="contact contact--right">
      <li>Email : your@name.com</li>
      <li>Twitter : twitterURL</li>
    </ul>
  </section>

</main>
</body>
</html>
```